West Calloway Commuter Services Alliance Needs an Ad Showcasing 2012's Accomplishments

The West Calloway Commuter Services Alliance is a nonprofit organization with the mission to foster transportation behaviors that benefit the community through advocacy, programs, education, and services. We have had a great year in 2012 and would like to show the community what we have accomplished.

We would like a FULL PAGE ad that will be used in a color print magazine and a black and white print publication.

The Pelican Loop - Over 75,000 trips taken by shuttle riders, a 120% increase in trips over 2011.

Stride Together Program - During the 2011-2012 school year an average of 897 students walked to school weekly on walk to school days.

Pedal Season Challenge - 41,950 miles were ridden by students and teachers in May 2012 in 9 participating schools.

Wheel Medic - over 600 bikes have been serviced in 2012.

Requirements
Must have
• Contact info:
West Calloway CSA
4827 Ramble Creek Rd
Marlowe Glen, CA 95870
916-555-0173
WCCSA.org

Twitter @West CallowayCSA
Facebook.com/WestCallowayCSA

LOGO

```html
<!DOCTYPE html>
<html lang="en">
<head>
<meta charset="utf-8">
<title>West Calloway CSA – 2012 Accomplishments</title>
<link rel="stylesheet" href="https://fonts.googleapis.com/css2?family=Source+Sans+3:wght@400;700&display=swap">
<style>
  :root {
    --stage: #3a3a3a;
    --paper: #ffffff;
    --sky-top: #1a5fc4;
    --sky-bottom: #7fc0f0;
    --band-orange: #f28c00;
    --line-blue: #2a6cc0;
    --line-green: #8cbf26;
    --title-green: #93b81c;
    --body-ink: #4a4a55;
    --tick-gold: #f5b323;
    --tick-edge: #d98a10;
    --logo-blue: #2d5aa8;
    --footer-ink: #ffffff;
  }
  * { margin: 0; padding: 0; box-sizing: border-box; }
  html, body {
    width: 1200px; height: 907px; overflow: hidden;
    background: var(--stage);
    font-family: "Source Sans 3", "Myriad Pro", Arial, sans-serif;
  }
  .ad-page {
    position: absolute; left: 297px; top: 39px;
    width: 604px; height: 826px;
    background: var(--paper);
    overflow: hidden;
  }
  .ad-shapes { position: absolute; inset: 0; width: 604px; height: 826px; }
  .brand-mark {
    position: absolute; left: 218px; top: 111px;
    width: 134px; height: 134px;
    display: flex; align-items: center; justify-content: center;
    text-align: center;
    color: var(--logo-blue);
    font-weight: 700; font-size: 17px; line-height: 1.1;
  }
  .accomplishment {
    position: absolute; left: 68px; width: 510px;
  }
  .accomplishment-title {
    display: flex; align-items: center; gap: 0;
    color: var(--title-green);
    font-weight: 700; font-size: 25px; line-height: 28px;
    margin-left: -6px;
  }
  .tick { width: 44px; height: 32px; flex: none; margin-top: -8px; }
  .accomplishment-text {
    color: var(--body-ink);
    font-weight: 700; font-size: 21px; line-height: 25.5px;
  }
  .contact {
    position: absolute; left: 0; right: 0; top: 781px;
    text-align: center; color: var(--footer-ink);
    font-size: 11px; line-height: 14px;
  }
  .contact-name { font-weight: 700; }
</style>
</head>
<body>
<main class="ad-page">
  <svg class="ad-shapes" viewBox="0 0 515 705" preserveAspectRatio="none">
    <defs>
      <linearGradient id="sky" x1="0" y1="0" x2="0" y2="1">
        <stop offset="0" stop-color="var(--sky-top)"/>
        <stop offset="1" stop-color="var(--sky-bottom)"/>
      </linearGradient>
    </defs>
    <rect x="0" y="0" width="515" height="240" fill="url(#sky)" role="img"
          aria-label="Blue sky with a rainbow arching across, white clouds and a hot air balloon"/>
    <path d="M0,226 Q257,140 515,226 L515,705 L0,705 Z" fill="var(--paper)"/>
    <path d="M0,226 Q257,140 515,226" fill="none" stroke="var(--line-blue)" stroke-width="3"/>
    <path d="M0,230 Q257,144 515,230" fill="none" stroke="var(--band-orange)" stroke-width="1.5"/>
    <path d="M0,588 Q257,695 515,588 L515,705 L0,705 Z" fill="var(--band-orange)"/>
    <path d="M0,581 Q257,688 515,581" fill="none" stroke="var(--line-green)" stroke-width="2"/>
    <path d="M0,585 Q257,692 515,585" fill="none" stroke="var(--line-blue)" stroke-width="3"/>
    <circle cx="243" cy="152" r="56" fill="var(--paper)" stroke="var(--band-orange)" stroke-width="2"/>
  </svg>

  <div class="brand-mark">West Calloway<br>CSA</div>

  <section class="accomplishment" style="top:294px">
    <h2 class="accomplishment-title"><svg class="tick" viewBox="0 0 44 32"><path d="M3,17 L14,28 L41,3 L14,19 Z" fill="var(--tick-gold)" stroke="var(--tick-edge)" stroke-width="1.5" stroke-linejoin="round"/></svg>The Pelican Loop</h2>
    <p class="accomplishment-text">Over 75,000 trips taken by shuttle riders,<br>a 120% increase in trips over 2011</p>
  </section>

  <section class="accomplishment" style="top:401px">
    <h2 class="accomplishment-title"><svg class="tick" viewBox="0 0 44 32"><path d="M3,17 L14,28 L41,3 L14,19 Z" fill="var(--tick-gold)" stroke="var(--tick-edge)" stroke-width="1.5" stroke-linejoin="round"/></svg>Stride Together Program</h2>
    <p class="accomplishment-text">During the 2011-2012 school year an average of<br>897 students walked to school weekly on walk<br>to school days</p>
  </section>

  <section class="accomplishment" style="top:534px">
    <h2 class="accomplishment-title"><svg class="tick" viewBox="0 0 44 32"><path d="M3,17 L14,28 L41,3 L14,19 Z" fill="var(--tick-gold)" stroke="var(--tick-edge)" stroke-width="1.5" stroke-linejoin="round"/></svg>Pedal Season Challenge</h2>
    <p class="accomplishment-text">41,950 miles were ridden by students and teach-<br>ers in May 2012 in 9 participating schools.</p>
  </section>

  <section class="accomplishment" style="top:640px">
    <h2 class="accomplishment-title"><svg class="tick" viewBox="0 0 44 32"><path d="M3,17 L14,28 L41,3 L14,19 Z" fill="var(--tick-gold)" stroke="var(--tick-edge)" stroke-width="1.5" stroke-linejoin="round"/></svg>Wheel Medic</h2>
    <p class="accomplishment-text">Over 600 bikes have been serviced in 2012</p>
  </section>

  <footer class="contact">
    <div class="contact-name">West Calloway CSA</div>
    <div>4827 Ramble Creek Rd; Marlowe Glen, CA 95870; 916-555-0173</div>
    <div>WCCSA.org</div>
  </footer>
</main>
</body>
</html>
```